Business Card Design for Online Gift Business

Business card design for a new online Canadian company called "Harlow & Reed Gift Crates" selling modern and luxurious gift boxes for every occasion. Items are sourced locally from talented socially-responsible Canadian artisans. Each gift is elegantly presented in a keepsake wood box to ensure a lasting impression.

Industry/Entity Type

E-Commerce

Contact Information for Business Card

Merin Holloway, Proprietor
Calgary, AB
587-214-3306
www.harlowandreed.ca
hello@harlowandreed.ca

Requirements
Must have
• Gifts from our best, to your best
• Please also include the symbols for Facebook and Instagram
Nice to have
• **I have attached a few samples of background colors and font colors that I like. I hope this helps in a few directions to try.

```html
<!DOCTYPE html>
<html lang="en">
<head>
<meta charset="utf-8">
<title>Harlow &amp; Reed Gift Crates — Business Card</title>
<link rel="stylesheet" href="https://fonts.googleapis.com/css2?family=Questrial&display=swap">
<style>
  :root {
    --page-bg: #f1ede8;
    --card-light: #ece1d2;
    --card-mid: #e3d5c2;
    --copper: #b8763a;
    --ink: #3a3633;
    --ink-soft: #5a5450;
    --ribbon-dark: #2b2a2a;
    --ribbon-light: #d9d2c8;
    --edge: #cfc3b2;
  }
  * { box-sizing: border-box; margin: 0; padding: 0; }
  html, body { width: 1200px; height: 1000px; overflow: hidden; }
  body {
    background: var(--page-bg);
    font-family: "Questrial", "Century Gothic", sans-serif;
    color: var(--ink);
    position: relative;
  }
  .card {
    position: absolute;
    width: 600px;
    height: 343px;
    background: linear-gradient(100deg, var(--card-light), var(--card-mid));
    border: 1px solid var(--edge);
    box-shadow: 0 10px 24px rgba(60, 45, 30, 0.18);
    overflow: hidden;
  }
  .card--front { left: 80px; top: 110px; }
  .card--back { left: 520px; top: 540px; }

  /* ribbon on front */
  .ribbon { position: absolute; left: 70px; top: 0; width: 70px; height: 100%; }
  .ribbon__stripe { position: absolute; top: 0; width: 7px; height: 100%; background: var(--ribbon-dark); }
  .ribbon__stripe--left { left: 10px; }
  .ribbon__stripe--right { left: 52px; }
  .ribbon__band { position: absolute; left: 17px; top: 0; width: 35px; height: 100%; background: var(--ribbon-light); }
  .ribbon__bow {
    position: absolute; left: -18px; top: 120px; width: 110px; height: 120px;
    border-radius: 40% 45% 40% 45%;
    background: radial-gradient(circle at 50% 50%, #f2eee8 0%, #cfc7bc 55%, #6f6a64 100%);
  }

  /* wordmark */
  .wordmark {
    color: var(--copper);
    font-family: "Questrial", "Century Gothic", sans-serif;
    letter-spacing: 0.12em;
    text-transform: uppercase;
    white-space: nowrap;
  }
  .card--front .wordmark { position: absolute; left: 232px; top: 70px; font-size: 30px; }
  .wordmark__dot {
    display: inline-block; width: 12px; height: 12px; border-radius: 50%;
    background: var(--copper); margin-left: 8px; vertical-align: middle;
  }

  .holder { position: absolute; left: 232px; top: 168px; display: flex; align-items: baseline; gap: 14px; }
  .holder__name { font-size: 22px; letter-spacing: 0.04em; text-transform: uppercase; color: var(--ink); }
  .holder__role { font-size: 15px; color: var(--ink-soft); }

  .contact { position: absolute; left: 262px; top: 210px; list-style: none; }
  .contact li { display: flex; align-items: center; gap: 10px; font-size: 16px; color: var(--ink-soft); line-height: 26px; }
  .contact svg { width: 14px; height: 14px; fill: var(--ink); flex: none; }

  /* back */
  .card--back .wordmark {
    position: absolute; left: 0; right: 0; top: 92px; text-align: center; font-size: 42px;
  }
  .web {
    position: absolute; left: 0; right: 0; top: 164px; text-align: center;
    font-size: 18px; letter-spacing: 0.22em; color: var(--ink-soft);
  }
  .tagline {
    position: absolute; left: 0; right: 0; top: 204px; text-align: center;
    font-size: 16px; letter-spacing: 0.06em; color: var(--copper);
  }
  .social {
    position: absolute; left: 0; right: 0; top: 246px;
    display: flex; justify-content: center; gap: 14px; list-style: none;
  }
  .social__link {
    width: 24px; height: 24px; border-radius: 50%; background: var(--ink-soft);
  }
</style>
</head>
<body>
  <section class="card card--front" aria-label="Business card front">
    <div class="ribbon">
      <div class="ribbon__band"></div>
      <div class="ribbon__stripe ribbon__stripe--left"></div>
      <div class="ribbon__stripe ribbon__stripe--right"></div>
      <div class="ribbon__bow" role="img" aria-label="Satin ribbon bow tied around the card"></div>
    </div>

    <div class="wordmark">Harlow &amp; Reed<span class="wordmark__dot"></span></div>

    <div class="holder">
      <span class="holder__name">Merin Holloway</span>
      <span class="holder__role">Proprietor</span>
    </div>

    <ul class="contact">
      <li>
        <svg viewBox="0 0 24 24" aria-hidden="true"><path d="M12 2a7 7 0 0 0-7 7c0 5 7 13 7 13s7-8 7-13a7 7 0 0 0-7-7zm0 9.5A2.5 2.5 0 1 1 12 6.5a2.5 2.5 0 0 1 0 5z"/></svg>
        Calgary, AB
      </li>
      <li>
        <svg viewBox="0 0 24 24" aria-hidden="true"><path d="M6.6 10.8a15 15 0 0 0 6.6 6.6l2.2-2.2a1 1 0 0 1 1-.25 11 11 0 0 0 3.6.6 1 1 0 0 1 1 1V20a1 1 0 0 1-1 1A17 17 0 0 1 3 4a1 1 0 0 1 1-1h3.5a1 1 0 0 1 1 1 11 11 0 0 0 .6 3.6 1 1 0 0 1-.25 1z"/></svg>
        587-214-3306
      </li>
      <li>
        <svg viewBox="0 0 24 24" aria-hidden="true"><path d="M12 2a10 10 0 1 0 0 20 10 10 0 0 0 0-20zm6.9 9h-3a15 15 0 0 0-1.3-6A8 8 0 0 1 18.9 11zM12 4c.9 1.2 1.7 3.6 1.9 7h-3.8c.2-3.4 1-5.8 1.9-7zM9.4 5a15 15 0 0 0-1.3 6h-3A8 8 0 0 1 9.4 5zM5.1 13h3a15 15 0 0 0 1.3 6A8 8 0 0 1 5.1 13zM12 20c-.9-1.2-1.7-3.6-1.9-7h3.8c-.2 3.4-1 5.8-1.9 7zm2.6-1a15 15 0 0 0 1.3-6h3a8 8 0 0 1-4.3 6z"/></svg>
        www.harlowandreed.ca
      </li>
      <li>
        <svg viewBox="0 0 24 24" aria-hidden="true"><path d="M3 5h18a1 1 0 0 1 1 1v12a1 1 0 0 1-1 1H3a1 1 0 0 1-1-1V6a1 1 0 0 1 1-1zm9 7.5L4 7.3V17h16V7.3z"/></svg>
        hello@harlowandreed.ca
      </li>
    </ul>
  </section>

  <section class="card card--back" aria-label="Business card back">
    <div class="wordmark">Harlow &amp; Reed<span class="wordmark__dot"></span></div>
    <p class="web">www.harlowandreed.ca</p>
    <p class="tagline">Gifts from our best, to your best</p>
    <ul class="social">
      <li class="social__link" role="img" aria-label="Social profile icon placeholder"></li>
      <li class="social__link" role="img" aria-label="Social profile icon placeholder"></li>
    </ul>
  </section>
</body>
</html>
```